3 out of 100 people will get deadly skin cancer - we need a great illustration that shows this!

We put together a prototype image that communicates lifetime skin cancer risk. (see attached). We are looking for illustrators who can take make a new/better/cooler graphic that communicates this idea. It could be as simple as a superior illustration of the graphic we have or illustrators can propose a completely different idea.What should the illustration communicate?U.S. adults have a lifetime risk of developing skin cancer of 1 in 5. But we don't want to show 1 in 5; we want to show that number in a larger group. For example, in the attached illustration we show 20 in 100 people get skin cancer (i.e., 100 beach towels/umbrellas and 20 of them are red). Research has shown that people are more likely to accurately understand numbers like this when you convey them for larger groups (i.e., 20 out of 100 rather than 1 out of 5). U.S. adults also have a lifetime risk of 2.3% of developing the deadliest form of skin cancer (melanoma). In other words, approximately 3 in 100 people will develop melanoma in their lifetime. Ideally, a single image will convey both lifetime skin cancer risk (20 in 100) and melanoma risk (3 in 100). We will award a top three as follows: 1st place = $300, 2nd place = $250, third place = $200. We will also buy any design beyond 3rd place that we like for $100. For example, we purchased 24 designs in our last contest on Artmarketly.This research is supported by funding from the Corvane Institute of Science.

Target Market(s)

The U.S. public; individuals at high risk of developing skin cancer

Industry/Entity Type

Medicine

Colors

Designer to choose colors to be used in the design.

Requirements
Must have
• an original illustration that conveys both lifetime risk of developing skin cancer (20 in 100) and melanoma (3 in 100).
Nice to have
• It can be beach towels and umbrellas, just like our prototype, or the designers can pitch an original idea. Imagery can be realistic or cartoonish (or something in between). It should be illustrations, though. Not edited photos. The image should be in color (no black and white illustrations).
Should not have
• Photos. Clip art. Free vector images.
• We are looking for original illustrations created by the designer.

```html
<!DOCTYPE html>
<html lang="en">
<head>
<meta charset="utf-8">
<title>Skin Cancer – Lifetime Risk and Prevention</title>
<link href="https://fonts.googleapis.com/css2?family=Roboto:ital,wght@0,400;0,500;0,700;0,900;1,400&display=swap" rel="stylesheet">
<style>
  :root {
    --navy: #1a64a8;
    --navy-deep: #14558f;
    --peach: #f6cf95;
    --peach-light: #f9dcae;
    --skin: #f5cf9f;
    --sun-blue: #1f73b7;
    --alert-red: #d0202a;
    --risk-red: #c21f2b;
    --melanoma: #2b2b2b;
    --sky-top: #3aa7e4;
    --sky-mid: #bfe3f6;
    --sea: #7dd0e6;
    --sand: #f0c98d;
    --sand-deep: #eab677;
    --ink: #1c2430;
    --subtitle-blue: #2a7fc2;
    --pale-blue: #a9dcf3;
    --tip-blue: #5ccaf5;
    --card-white: #f4f7fa;
    --card-pink: #f4d3dc;
    --label-blue: #3e6fa6;
    --crowd-bg: #fbf3e6;
    --white: #ffffff;
  }
  * { margin: 0; padding: 0; box-sizing: border-box; }
  html, body { width: 1200px; height: 4412px; overflow: hidden; }
  body { font-family: "Roboto", Arial, sans-serif; color: var(--ink); background: var(--tip-blue); }
  .poster { position: relative; width: 1200px; height: 4412px; }

  .masthead {
    position: absolute; left: 0; top: 0; width: 1200px; height: 182px;
    background: var(--navy);
    display: flex; align-items: center; justify-content: center;
  }
  .masthead h1 { color: var(--white); font-weight: 900; font-size: 96px; letter-spacing: 1px; }

  .facts { position: absolute; left: 0; top: 182px; width: 1200px; height: 398px; background: var(--peach); }
  .fact { position: absolute; left: 338px; width: 760px; font-weight: 700; font-size: 37px; line-height: 50px; color: var(--ink); }
  .fact em { font-style: normal; color: var(--alert-red); }
  .fact-one { top: 66px; }
  .fact-two { top: 258px; }
  .sun-icon { position: absolute; }
  .sun-one { left: 176px; top: 82px; width: 118px; height: 118px; }
  .sun-two { left: 165px; top: 265px; width: 140px; height: 140px; }

  .beach {
    position: absolute; left: 0; top: 580px; width: 1200px; height: 1693px;
    background: linear-gradient(180deg, var(--sky-top) 0%, var(--sky-mid) 22%, var(--white) 38%, var(--white) 44%, var(--sea) 46%, var(--sea) 48%, var(--sand) 52%, var(--sand-deep) 100%);
  }
  .beach-question {
    position: absolute; left: 200px; top: 100px; width: 805px; height: 122px;
    background: var(--navy-deep);
    display: flex; align-items: center; justify-content: center;
    color: var(--white); font-weight: 700; font-size: 44px;
  }
  .beach-lead { position: absolute; left: 0; top: 230px; width: 1200px; text-align: center; color: var(--subtitle-blue); font-size: 38px; font-weight: 500; }
  .beach-questions { position: absolute; left: 56px; top: 287px; list-style: none; font-size: 30px; line-height: 47px; color: var(--ink); }
  .beach-questions li::before { content: "• "; }

  .legend {
    position: absolute; left: 229px; top: 414px; width: 741px; height: 276px;
    background: var(--card-white); border-radius: 14px;
    box-shadow: 0 6px 18px rgba(40, 80, 120, 0.18);
    display: flex; overflow: hidden;
  }
  .legend-item { flex: 1; display: flex; flex-direction: column; align-items: center; }
  .legend-item.is-cancer { background: var(--card-pink); }
  .legend-figure { width: 120px; height: 150px; margin-top: 30px; border-radius: 56px 56px 10px 10px; }
  .figure-clear { background: var(--skin); }
  .figure-cancer { background: var(--risk-red); }
  .figure-melanoma { background: var(--melanoma); }
  .legend-label { margin-top: 20px; text-align: center; color: var(--label-blue); font-size: 25px; line-height: 28px; font-style: italic; text-transform: uppercase; }

  .crowd { position: absolute; left: 194px; top: 808px; width: 811px; height: 832px; background: var(--crowd-bg); }
  .crowd svg { display: block; width: 811px; height: 832px; }
  .mark-clear { fill: var(--skin); }
  .mark-cancer { fill: var(--risk-red); }
  .mark-melanoma { fill: var(--melanoma); }

  .prevention-head { position: absolute; left: 0; top: 2273px; width: 1200px; height: 345px; background: var(--pale-blue); }
  .prevention-title {
    position: absolute; left: 200px; top: 10px; width: 805px; height: 106px;
    background: var(--navy); color: var(--white);
    display: flex; align-items: center; padding-left: 34px;
    font-weight: 700; font-size: 40px;
  }
  .prevention-intro { position: absolute; left: 223px; top: 164px; width: 860px; font-weight: 700; font-size: 35px; line-height: 47px; color: var(--ink); }

  .tip { position: absolute; left: 200px; width: 805px; }
  .tip-heading {
    height: 60px; background: var(--navy); color: var(--white);
    display: flex; align-items: center; gap: 20px; padding-left: 24px;
    font-weight: 700; font-size: 38px;
  }
  .tip-heading::before { content: ""; width: 18px; height: 18px; border-radius: 50%; background: var(--pale-blue); }
  .tip-body { margin-top: 4px; padding-left: 62px; font-size: 37px; line-height: 51px; font-weight: 500; color: var(--ink); white-space: nowrap; }
  .tip-sun { top: 2675px; }
  .tip-sunscreen { top: 3005px; }
  .tip-clothing { top: 3334px; }
  .tip-tanning { top: 3719px; }
  .tip-selfcheck { top: 4048px; }
</style>
</head>
<body>
<main class="poster">

  <header class="masthead"><h1>SKIN CANCER</h1></header>

  <section class="facts">
    <svg class="sun-icon sun-one" viewBox="0 0 100 100" aria-hidden="true">
      <circle cx="50" cy="50" r="22" fill="var(--sun-blue)"/>
      <g stroke="var(--sun-blue)" stroke-width="4" stroke-linecap="round">
        <line x1="50" y1="4" x2="50" y2="20"/><line x1="50" y1="80" x2="50" y2="96"/>
        <line x1="4" y1="50" x2="20" y2="50"/><line x1="80" y1="50" x2="96" y2="50"/>
        <line x1="17" y1="17" x2="28" y2="28"/><line x1="72" y1="72" x2="83" y2="83"/>
        <line x1="83" y1="17" x2="72" y2="28"/><line x1="28" y1="72" x2="17" y2="83"/>
      </g>
    </svg>
    <p class="fact fact-one">The primary cause of skin cancer is<br>exposure to <em>ultraviolet (UV)</em> Light<br>from the sun or indoor tanning.</p>

    <svg class="sun-icon sun-two" viewBox="0 0 100 100" aria-hidden="true">
      <circle cx="50" cy="50" r="24" fill="var(--sun-blue)"/>
      <g fill="var(--sun-blue)">
        <polygon points="50,2 54,22 46,22"/><polygon points="50,98 54,78 46,78"/>
        <polygon points="2,50 22,46 22,54"/><polygon points="98,50 78,46 78,54"/>
        <polygon points="16,16 32,28 28,32"/><polygon points="84,84 68,72 72,68"/>
        <polygon points="84,16 72,32 68,28"/><polygon points="16,84 28,68 32,72"/>
      </g>
    </svg>
    <p class="fact fact-two">The greater the total amount of sun<br>exposure over a lifetime, the greater<br>the change of <em>MELANOMA</em>.</p>
  </section>

  <section class="beach">
    <h2 class="beach-question">How likely are you get skin cancer?</h2>
    <p class="beach-lead">Lest’s say 100 people go to the beach...</p>
    <ul class="beach-questions">
      <li>How many will develop skin cancer in their lifetime?</li>
      <li>How many will develop melanoma, the deadliest from skin cancer?</li>
    </ul>

    <div class="legend">
      <div class="legend-item">
        <div class="legend-figure figure-clear" role="img" aria-label="Marker for a person with no skin cancer"></div>
        <span class="legend-label">No skin<br>cancer</span>
      </div>
      <div class="legend-item is-cancer">
        <div class="legend-figure figure-cancer" role="img" aria-label="Marker for a person with skin cancer"></div>
        <span class="legend-label">Skin cancer</span>
      </div>
      <div class="legend-item">
        <div class="legend-figure figure-melanoma" role="img" aria-label="Marker for a person with melanoma"></div>
        <span class="legend-label">Melanoma</span>
      </div>
    </div>

    <div class="crowd">
      <svg viewBox="0 0 811 832" role="img" aria-label="100 people: 77 with no skin cancer, 20 with skin cancer in red, 3 with melanoma in black">
        <defs>
          <rect id="m" x="-26" y="-34" width="52" height="68" rx="22"/>
        </defs>
        <!-- row 1 -->
        <g transform="translate(0,47)">
          <use href="#m" x="91" class="mark-clear"/><use href="#m" x="161" class="mark-cancer"/><use href="#m" x="231" class="mark-clear"/><use href="#m" x="301" class="mark-clear"/><use href="#m" x="371" class="mark-cancer"/><use href="#m" x="441" class="mark-clear"/><use href="#m" x="511" class="mark-clear"/><use href="#m" x="581" class="mark-clear"/><use href="#m" x="651" class="mark-clear"/><use href="#m" x="721" class="mark-clear"/>
        </g>
        <!-- row 2 -->
        <g transform="translate(0,131)">
          <use href="#m" x="91" class="mark-clear"/><use href="#m" x="161" class="mark-clear"/><use href="#m" x="231" class="mark-clear"/><use href="#m" x="301" class="mark-clear"/><use href="#m" x="371" class="mark-clear"/><use href="#m" x="441" class="mark-melanoma"/><use href="#m" x="511" class="mark-clear"/><use href="#m" x="581" class="mark-clear"/><use href="#m" x="651" class="mark-clear"/><use href="#m" x="721" class="mark-cancer"/>
        </g>
        <!-- row 3 -->
        <g transform="translate(0,215)">
          <use href="#m" x="91" class="mark-cancer"/><use href="#m" x="161" class="mark-clear"/><use href="#m" x="231" class="mark-clear"/><use href="#m" x="301" class="mark-clear"/><use href="#m" x="371" class="mark-clear"/><use href="#m" x="441" class="mark-clear"/><use href="#m" x="511" class="mark-clear"/><use href="#m" x="581" class="mark-clear"/><use href="#m" x="651" class="mark-clear"/><use href="#m" x="721" class="mark-cancer"/>
        </g>
        <!-- row 4 -->
        <g transform="translate(0,299)">
          <use href="#m" x="91" class="mark-clear"/><use href="#m" x="161" class="mark-clear"/><use href="#m" x="231" class="mark-clear"/><use href="#m" x="301" class="mark-clear"/><use href="#m" x="371" class="mark-clear"/><use href="#m" x="441" class="mark-clear"/><use href="#m" x="511" class="mark-clear"/><use href="#m" x="581" class="mark-cancer"/><use href="#m" x="651" class="mark-clear"/><use href="#m" x="721" class="mark-clear"/>
        </g>
        <!-- row 5 -->
        <g transform="translate(0,383)">
          <use href="#m" x="91" class="mark-clear"/><use href="#m" x="161" class="mark-clear"/><use href="#m" x="231" class="mark-cancer"/><use href="#m" x="301" class="mark-clear"/><use href="#m" x="371" class="mark-clear"/><use href="#m" x="441" class="mark-clear"/><use href="#m" x="511" class="mark-clear"/><use href="#m" x="581" class="mark-clear"/><use href="#m" x="651" class="mark-cancer"/><use href="#m" x="721" class="mark-melanoma"/>
        </g>
        <!-- row 6 -->
        <g transform="translate(0,467)">
          <use href="#m" x="91" class="mark-clear"/><use href="#m" x="161" class="mark-clear"/><use href="#m" x="231" class="mark-clear"/><use href="#m" x="301" class="mark-clear"/><use href="#m" x="371" class="mark-clear"/><use href="#m" x="441" class="mark-cancer"/><use href="#m" x="511" class="mark-clear"/><use href="#m" x="581" class="mark-clear"/><use href="#m" x="651" class="mark-clear"/><use href="#m" x="721" class="mark-clear"/>
        </g>
        <!-- row 7 -->
        <g transform="translate(0,551)">
          <use href="#m" x="91" class="mark-cancer"/><use href="#m" x="161" class="mark-clear"/><use href="#m" x="231" class="mark-clear"/><use href="#m" x="301" class="mark-cancer"/><use href="#m" x="371" class="mark-clear"/><use href="#m" x="441" class="mark-cancer"/><use href="#m" x="511" class="mark-clear"/><use href="#m" x="581" class="mark-clear"/><use href="#m" x="651" class="mark-cancer"/><use href="#m" x="721" class="mark-clear"/>
        </g>
        <!-- row 8 -->
        <g transform="translate(0,635)">
          <use href="#m" x="91" class="mark-clear"/><use href="#m" x="161" class="mark-clear"/><use href="#m" x="231" class="mark-clear"/><use href="#m" x="301" class="mark-clear"/><use href="#m" x="371" class="mark-clear"/><use href="#m" x="441" class="mark-clear"/><use href="#m" x="511" class="mark-cancer"/><use href="#m" x="581" class="mark-clear"/><use href="#m" x="651" class="mark-clear"/><use href="#m" x="721" class="mark-cancer"/>
        </g>
        <!-- row 9 -->
        <g transform="translate(0,719)">
          <use href="#m" x="91" class="mark-clear"/><use href="#m" x="161" class="mark-clear"/><use href="#m" x="231" class="mark-cancer"/><use href="#m" x="301" class="mark-clear"/><use href="#m" x="371" class="mark-cancer"/><use href="#m" x="441" class="mark-clear"/><use href="#m" x="511" class="mark-clear"/><use href="#m" x="581" class="mark-cancer"/><use href="#m" x="651" class="mark-clear"/><use href="#m" x="721" class="mark-clear"/>
        </g>
        <!-- row 10 -->
        <g transform="translate(0,795)">
          <use href="#m" x="91" class="mark-clear"/><use href="#m" x="161" class="mark-clear"/><use href="#m" x="231" class="mark-melanoma"/><use href="#m" x="301" class="mark-clear"/><use href="#m" x="371" class="mark-clear"/><use href="#m" x="441" class="mark-cancer"/><use href="#m" x="511" class="mark-clear"/><use href="#m" x="581" class="mark-clear"/><use href="#m" x="651" class="mark-clear"/><use href="#m" x="721" class="mark-cancer"/>
        </g>
      </svg>
    </div>
  </section>

  <section class="prevention-head">
    <h2 class="prevention-title">What can you do to prevent skin cancer</h2>
    <p class="prevention-intro">Leading medical expert, including<br>those at Halvern Clinic, make these recom-<br>medations for preventing skin cancer:</p>
  </section>

  <article class="tip tip-sun">
    <h3 class="tip-heading">Avoid the sun from 10a.m to 4p.m.</h3>
    <p class="tip-body">These are the peak hours of sun<br>strength in north america-even in the<br>winter and on cloudy days.</p>
  </article>
  <article class="tip tip-sunscreen">
    <h3 class="tip-heading">Wear sunscreen</h3>
    <p class="tip-body">Reapply sunscreen every two hours or<br>more frequently if you are swimming<br>or sweating.</p>
  </article>
  <article class="tip tip-clothing">
    <h3 class="tip-heading">Wear protective clothing</h3>
    <p class="tip-body">Hats with wide brims and clothing that<br>covers your arms and legs are helpful.<br>Sunscreen does not block all UV rays,<br>which caused skin cancer.</p>
  </article>
  <article class="tip tip-tanning">
    <h3 class="tip-heading">Avoid tanning bed</h3>
    <p class="tip-body">Tanning beds operate with UV Lights,<br>damaging your skin and potentially<br>leading to cancer.</p>
  </article>
  <article class="tip tip-selfcheck">
    <h3 class="tip-heading">Self-check your skin</h3>
    <p class="tip-body">If you notice differences, talk with your<br>health care team.</p>
  </article>

</main>
</body>
</html>
```